添付の車の荷台部分とその際のドライブスルーのデザインになります。
合計2か所
添付のデザインイメージでお願いいたします。
・トラック看板寸法 3020×1800
・ドライブスルー看板 8280×1230
ドライブスルー看板のサイズが間違っていましたので、
再度はかってからまた記載させていただきます。

添付した写真「ドライブスルー 看板」が実際に使用する看板です。
ドライブスルーサイズ
誤りがありました!
正しくは

830×1230
です!

デザインが素敵でした。

今後ともよろしくお願いいたします。

```html
<!DOCTYPE html>
<html lang="ja">
<head>
<meta charset="UTF-8">
<title>ルナリ LUNARI ドライブスルー看板</title>
<link rel="stylesheet" href="https://fonts.googleapis.com/css2?family=Noto+Sans+JP:wght@900&display=swap">
<style>
  :root {
    --bg: #5b6f97;
    --paper: #ffffff;
  }
  html, body {
    margin: 0;
    padding: 0;
    overflow: hidden;
    background: var(--bg);
  }
  .sign {
    position: relative;
    width: 814px;
    height: 1200px;
    background: var(--bg);
    overflow: hidden;
    font-family: "Noto Sans JP", sans-serif;
    font-weight: 900;
    color: var(--paper);
  }
  .menu-points {
    position: absolute;
    left: 48px;
    top: 22px;
    margin: 0;
    padding: 0;
    list-style: none;
    font-size: 32px;
    line-height: 70px;
    letter-spacing: 1px;
  }
  .brand-name {
    position: absolute;
    left: 0;
    width: 814px;
    top: 270px;
    margin: 0;
    text-align: center;
    font-size: 150px;
    line-height: 1.15;
    letter-spacing: 8px;
  }
  .brand-name .latin {
    display: block;
    font-size: 124px;
    letter-spacing: 14px;
  }
  .products {
    position: absolute;
    left: 0;
    width: 814px;
    top: 690px;
    margin: 0;
    text-align: center;
    font-size: 46px;
    line-height: 62px;
    letter-spacing: 2px;
  }
  .drive-thru {
    position: absolute;
    left: 0;
    top: 0;
  }
  .hours {
    position: absolute;
    left: 380px;
    top: 1008px;
    font-size: 36px;
    letter-spacing: 1px;
  }
  .local-note {
    position: absolute;
    left: 54px;
    top: 1098px;
    margin: 0;
    font-size: 34px;
    letter-spacing: 1px;
  }
</style>
</head>
<body>
<main class="sign">
  <ul class="menu-points">
    <li>・炭を使った黒のフルーツサンドイッチ！</li>
    <li>・炭を使った黒のばななジュース！</li>
  </ul>

  <h1 class="brand-name">ルナリ<span class="latin">LUNARI</span></h1>

  <p class="products">炭サンドイッチ＆<br>炭ばななジュース</p>

  <svg class="drive-thru" width="814" height="1200" viewBox="0 0 814 1200" aria-label="DRIVE THRU">
    <polygon points="52,1022 140,984 140,1060" fill="var(--paper)"/>
    <text x="150" y="1012" font-family="Noto Sans JP, sans-serif"
          font-weight="900" font-size="54" fill="var(--paper)">DRIVE</text>
    <text x="150" y="1068" font-family="Noto Sans JP, sans-serif"
          font-weight="900" font-size="54" fill="var(--paper)">THRU</text>
    <line x1="366" y1="962" x2="366" y2="1078" stroke="var(--paper)" stroke-width="3"/>
    <line x1="366" y1="962" x2="814" y2="962" stroke="var(--paper)" stroke-width="3"/>
  </svg>

  <div class="hours">OPEN 8:00～23:00</div>

  <p class="local-note">地 元千葉流山初出店！</p>
</main>
</body>
</html>
```